Social Media Graphics - ALL TEXT RK

We are looking for a series of social media graphics for Instagram (standard size 1:1 (1080x1080px) that are ALL TEXT. We want the following quotes below on each graphic; one quote per graphic. AND, In very small letters at the bottom of each graphic, add @RKMarlowLive

The look and feel of these graphics should be complimentary to the color palette attached below; but keep them simple. But the design is up to you; at the end of this document, I provided various samples of all text graphics that I like as examples.

Target Market(s)

women looking to lose weight

Industry/Entity Type

health and wellness

Colors
E54698
E96AAD
F1A4CE
F9D9EA
FCEFF6

Requirements
Must have
• the quotes in the document
Should not have
• no stock photography

```html
<!DOCTYPE html>
<html lang="en">
<head>
<meta charset="utf-8">
<title>That Stubborn Belly Fat Isn't Your Fault</title>
<link href="https://fonts.googleapis.com/css2?family=Bungee&family=Poiret+One&family=Montserrat:ital,wght@0,800;0,900;1,800&family=Yellowtail&family=Damion&display=swap" rel="stylesheet">
<style>
  :root {
    --pink-deep: #E54698;
    --pink-mid: #E96AAD;
    --pink-soft: #F1A4CE;
    --pink-pale: #F9D9EA;
    --pink-mist: #FCEFF6;
    --white: #ffffff;
  }
  * { margin: 0; padding: 0; box-sizing: border-box; }
  html, body { width: 1200px; height: 1200px; overflow: hidden; }
  body {
    position: relative;
    background: linear-gradient(225deg, var(--pink-deep) 0%, var(--pink-soft) 50%, var(--pink-mist) 100%);
  }
  .poster-bg {
    position: absolute; inset: 0;
    background: linear-gradient(45deg, var(--pink-deep) 0%, var(--pink-soft) 45%, transparent 75%);
    opacity: 0.9;
  }
  .frame {
    position: absolute;
    left: 95px; top: 95px; width: 1010px; height: 1010px;
    border: 8px solid var(--pink-mist);
  }
  .band-top, .band-bottom {
    position: absolute; left: 155px; width: 890px;
  }
  .band-top { top: 155px; height: 278px; background: linear-gradient(135deg, var(--pink-mid), var(--pink-deep)); }
  .band-bottom { top: 768px; height: 277px; background: linear-gradient(45deg, var(--pink-deep), var(--pink-mid)); }
  .band-middle {
    position: absolute; left: 91px; top: 433px; width: 1018px; height: 335px;
    background: var(--pink-mist);
  }
  .handle-pill {
    position: absolute; left: 380px; top: 1063px; width: 440px; height: 84px;
    border-radius: 42px;
    background: var(--pink-pale);
    border: 8px solid var(--pink-mist);
  }
  .type-layer { position: absolute; left: 0; top: 0; width: 1200px; height: 1200px; }
  .tag-label { font-family: "Poiret One", sans-serif; font-weight: 700; font-size: 46px; fill: var(--pink-deep); stroke: var(--pink-deep); stroke-width: 1.6px; }
  .headline-that { font-family: "Bungee", sans-serif; font-size: 128px; fill: var(--pink-mist); }
  .headline-main { font-family: "Bungee", sans-serif; font-size: 112px; fill: var(--pink-deep); }
  .headline-fault { font-family: "Montserrat", sans-serif; font-weight: 900; font-size: 86px; fill: var(--white); }
  .subline { font-family: "Yellowtail", "Damion", cursive; font-size: 64px; fill: var(--white); }
  .handle { font-family: "Montserrat", sans-serif; font-weight: 800; font-style: italic; font-size: 42px; fill: var(--pink-deep); }
</style>
</head>
<body>
  <div class="poster-bg"></div>
  <div class="frame"></div>
  <div class="band-top"></div>
  <div class="band-middle"></div>
  <div class="band-bottom"></div>
  <div class="handle-pill"></div>

  <svg class="type-layer" viewBox="0 0 1200 1200" role="group" aria-label="That stubborn belly fat isn't your fault. Here's what no one tells you.">
    <polygon points="335,95 460,52 740,52 865,95 740,138 460,138" fill="var(--pink-mist)"/>
    <polygon points="356,95 463,60 737,60 844,95 737,130 463,130" fill="var(--pink-pale)"/>
    <text class="tag-label" x="449" y="114" textLength="299" lengthAdjust="spacingAndGlyphs">WEIGHT LOSS</text>

    <text class="headline-that" x="421" y="380" textLength="360" lengthAdjust="spacingAndGlyphs">THAT</text>
    <text class="headline-main" x="180" y="567" textLength="835" lengthAdjust="spacingAndGlyphs">STUBBORN</text>
    <text class="headline-main" x="184" y="707" textLength="827" lengthAdjust="spacingAndGlyphs">BELLY FAT</text>
    <text class="headline-fault" x="238" y="879" textLength="709" lengthAdjust="spacingAndGlyphs">ISN'T YOUR FAULT</text>
    <text class="subline" x="329" y="955" textLength="559" lengthAdjust="spacingAndGlyphs">here’s what no one tells you</text>

    <text class="handle" x="417" y="1120" textLength="364" lengthAdjust="spacingAndGlyphs">@RKMarlowLive</text>
  </svg>
</body>
</html>
```